We sell companies excess stock for them

We need a business card for a company based in New Zealand called 'StockHarbor'.

Check out our website to get an idea www.stockharbor.example

We help other businesses to;
- Sell Excess Stock
- Manage Product Returns
- Sell Company Assets

Our logo is attached for your reference
The font used is 'RifficFree-Bold'

Target Market(s)

Businesses

Industry/Entity Type

Business

Contact Information for Business Card

Name: Mark Pellow
Phone: 027 846 2093
email: markpellow@stockharbor.example
website: www.stockharbor.example

Font styles to use
Other font styles liked:
• Unsure

Colors
9bcb3b

Requirements
Must have
• coming soon
Nice to have
• coming soon
Should not have
• coming soon

```html
<!DOCTYPE html>
<html lang="en">
<head>
<meta charset="utf-8">
<title>StockHarbor Business Card</title>
<link href="https://fonts.googleapis.com/css2?family=Open+Sans:wght@400;600;700&display=swap" rel="stylesheet">
<style>
  :root {
    --page: #e9e7e4;
    --card: #1c1d1e;
    --card-edge: #2a2b2c;
    --green: #9bcb3b;
    --white: #f2f2f2;
    --grey: #bdbdbd;
    --rule: #6a6a6a;
  }
  * { box-sizing: border-box; margin: 0; padding: 0; }
  html, body {
    width: 1200px; height: 864px; overflow: hidden;
    background: var(--page);
    font-family: "Open Sans", Arial, sans-serif;
  }
  .canvas { position: relative; width: 1200px; height: 864px; }
  .card {
    position: absolute;
    width: 600px; height: 343px;
    background: var(--card);
    border: 1px solid var(--card-edge);
    border-radius: 4px;
    box-shadow: 0 10px 28px rgba(0,0,0,.25);
  }
  .card--front { left: 60px; top: 70px; }
  .card--back { left: 540px; top: 450px; }

  .brand {
    position: absolute;
    display: flex; align-items: center; gap: 14px;
  }
  .brand__mark {
    width: 54px; height: 54px; border-radius: 50%;
    background: linear-gradient(160deg, #8fbf3a, #d9a24a);
  }
  .brand__name {
    font-weight: 700; font-size: 50px; letter-spacing: -1px;
    color: var(--white); line-height: 1;
  }
  .card--front .brand { left: 120px; top: 96px; }
  .card--back .brand { left: 150px; top: 70px; }

  .tagline {
    position: absolute; left: 0; right: 0; top: 212px;
    text-align: center;
  }
  .tagline__lead {
    color: var(--green); font-weight: 600; font-size: 15px;
    letter-spacing: .3px; text-transform: uppercase;
  }
  .tagline__services {
    margin-top: 6px; color: var(--grey); font-size: 15px;
  }
  .tagline__rule {
    position: absolute; top: 230px; height: 1px; width: 70px;
    background: var(--rule);
  }
  .tagline__rule--left { left: 20px; }
  .tagline__rule--right { right: 20px; }

  .holder {
    position: absolute; left: 70px; top: 210px; width: 200px;
    text-align: right;
    color: var(--green); font-weight: 600; font-size: 19px;
    text-transform: uppercase; letter-spacing: .3px;
  }
  .divider {
    position: absolute; left: 290px; top: 196px;
    width: 1px; height: 78px; background: var(--rule);
  }
  .contacts {
    position: absolute; left: 310px; top: 204px;
    list-style: none;
  }
  .contacts li {
    display: flex; align-items: center; gap: 10px;
    color: var(--white); font-size: 15px; line-height: 22px;
  }
  .contacts svg { width: 14px; height: 14px; fill: var(--green); flex: none; }
</style>
</head>
<body>
<div class="canvas">

  <section class="card card--front">
    <div class="brand">
      <div class="brand__mark" role="img" aria-label="Brand mascot illustration"></div>
      <span class="brand__name">StockHarbor</span>
    </div>
    <span class="tagline__rule tagline__rule--left"></span>
    <span class="tagline__rule tagline__rule--right"></span>
    <div class="tagline">
      <p class="tagline__lead">We help other businesses to</p>
      <p class="tagline__services">Sell Excess Stock &bull; Manage Product Returns &bull; Sell Company Assets</p>
    </div>
  </section>

  <section class="card card--back">
    <div class="brand">
      <div class="brand__mark" role="img" aria-label="Brand mascot illustration"></div>
      <span class="brand__name">StockHarbor</span>
    </div>
    <p class="holder">Mark Pellow</p>
    <span class="divider"></span>
    <ul class="contacts">
      <li>
        <svg viewBox="0 0 16 16" aria-hidden="true"><path d="M3.6 1.5l2.3 2.6-1.2 1.8c.9 2 2.4 3.5 4.4 4.4l1.8-1.2 2.6 2.3-1.2 2.3C7 13.6 2.4 9 1.3 2.7z"/></svg>
        027 846 2093
      </li>
      <li>
        <svg viewBox="0 0 16 16" aria-hidden="true"><path d="M1 3h14v1.2L8 9 1 4.2z"/><path d="M1 5.6l7 4.8 7-4.8V13H1z"/></svg>
        markpellow@stockharbor.example
      </li>
      <li>
        <svg viewBox="0 0 16 16" aria-hidden="true"><path d="M8 1a7 7 0 1 0 0 14A7 7 0 0 0 8 1zm0 1.6c.9 0 1.9 1.7 2.2 4.4H5.8C6.1 4.3 7.1 2.6 8 2.6zm-2.2 6h4.4c-.3 2.7-1.3 4.4-2.2 4.4s-1.9-1.7-2.2-4.4z"/></svg>
        www.stockharbor.example
      </li>
    </ul>
  </section>

</div>
</body>
</html>
```